International Dental Education Website

This project is for a small teaching center on endodontic and micro dentistry in Norway. We need a Wordpress website design to display and highlight dental educational courses. Please use our new logo - see attached file. We like lighter, pastel oriented colors. The following sites are nicely laid out and you can use these as a guideline of sorts but I do want a unique site.
http://vorplex.example/en, http://www.toothmarlow.example/Education.aspx?currentSection=courses&cid=14,
http://www.pulpvesker.example/.
Please create a space for a possible video on the home page. Please include a small contact form on the home page(name, email, phone, text box). Would like a horizonatal naviagtion bar. Would like an image to go across the whole top part of the site and this may rotate. Please use a stock image that shows a classroom type setting. Put phone number at the top of the screen. Put address and sitemap in a footer.

Reason: Upcoming vacation with limited internet access. Please continue to submit any designs. Thanks you.

Reason: The client is from a foreign country and is on an extended vacation.

Target Market(s)

General dentists (GPs) and specialists in Endodontics

Industry/Entity Type

Dental

Requirements
Must have
• Sitemap: HOME, COURSES, LECTURER, CONTACT US,
NORWEGIAN/ENGLISH. Phone number is: +47 93516270. Business name and address: Kali Rom AS, Endodontic Teaching Center,
Fjeldstads vei 17C, 0371 Oslo, Norway.

```html
<!DOCTYPE html>
<html lang="en">
<head>
<meta charset="utf-8">
<title>Kali Rom – Endodontic Training Center</title>
<link href="https://fonts.googleapis.com/css2?family=Cabin:wght@400;600;700&family=Arimo:wght@400;700&family=Gelasio&display=swap" rel="stylesheet">
<style>
:root{
  --teal:#3aa9ad;--teal-light:#6cc7ca;--teal-dark:#2a8f93;
  --orange:#e8913c;--orange-dark:#c8692a;--title-orange:#e8823b;
  --red:#e8391e;--ink:#3a3a3a;--muted:#666;--line:#dcdcdc;
  --panel:#e4ebee;--footer:#637e8d;--footer-title:#7fe3ef;--white:#fff;
}
*{margin:0;padding:0;box-sizing:border-box}
html,body{width:914px;height:1200px;overflow:hidden}
body{position:relative;font-family:"Cabin",sans-serif;color:var(--ink);
  background:linear-gradient(#e3e7e9 0,#eef1f2 260px,#fff 420px,#fff 100%)}
.abs{position:absolute}
.topbar{left:0;top:0;width:914px;height:38px;background:linear-gradient(#78cfd2,#3aa6ab)}
.nav{left:295px;top:13px;font:700 13px "Arimo",sans-serif;color:var(--white)}
.nav a{position:absolute;white-space:nowrap;color:inherit;text-decoration:none}
.logo{left:123px;top:0;width:129px;height:115px;background:#f7f8f8;box-shadow:0 2px 4px rgba(0,0,0,.25);text-align:center}
.logo-name{display:block;margin-top:34px;font:700 24px "Cabin",sans-serif;color:var(--teal)}
.logo-tag{display:block;margin-top:12px;font-size:8px;color:#333}
.call{left:648px;top:72px}
.call-label{position:absolute;left:27px;top:0;font-size:13px;white-space:nowrap;color:#222}
.call-num{position:absolute;left:27px;top:13px;font:700 19px "Arimo",sans-serif;color:var(--red);white-space:nowrap}
.box{background:var(--white);border:1px solid var(--line);border-radius:3px}
.slider{left:120px;top:134px;width:444px;height:262px;border:2px solid #c9cccd;background:#fff}
.slide-img{left:13px;top:12px;width:415px;height:178px;background:linear-gradient(160deg,#d7dadc,#9aa0a5 55%,#4a4c50)}
.slide-caption{left:13px;top:164px;width:415px;height:26px;background:rgba(20,20,20,.7);color:#fff;font:15px "Gelasio",serif;padding:4px 7px}
.thumb{top:197px;width:129px;height:48px;background:#55585b}
.thumb.active{background:linear-gradient(#cfd3d6,#8c9297);border:2px solid #888}
.next{left:584px;top:134px;width:208px;height:212px;border:1px solid var(--line);background:#fff;padding:2px}
.next-head{height:36px;background:#4a4a4a;color:#fff;font-size:15px;padding:10px 13px}
.next-list{list-style:none;background:var(--orange);height:170px;padding:5px 10px 0 14px}
.next-list li{height:23px;border-bottom:1px solid #f0a862;color:#fff;font:700 10.5px "Arimo",sans-serif;padding:5px 0 0 18px;position:relative;white-space:nowrap;margin-right:18px}
.next-list li::before{content:"→";position:absolute;left:4px;top:4px;font-size:9px}
.next-list li:last-child{border:0}
.search{left:584px;top:368px;width:208px;height:28px;border-radius:3px;overflow:hidden;background:linear-gradient(90deg,#f5f2e8,#e8e6dd)}
.search span{position:absolute;left:6px;top:8px;font-size:11px;color:#444}
.search .go{position:absolute;right:0;top:0;width:66px;height:28px;background:var(--teal);clip-path:polygon(14px 0,100% 0,100% 100%,0 100%,0 60%);color:#fff;font:700 14px "Arimo",sans-serif;text-align:center;padding-top:6px;padding-left:8px}
.welcome{left:120px;top:416px;width:444px;height:282px}
.title-orange{font-size:19px;color:var(--title-orange);font-weight:400;letter-spacing:.4px}
.welcome h2{position:absolute;left:14px;top:11px}
.dots{position:absolute;left:14px;width:414px;border-top:1px dotted #ccc}
.welcome-img{left:14px;top:51px;width:172px;height:102px;border:2px solid #aab;background:linear-gradient(#e9eef2,#9fb0bf 60%,#2b3440)}
.text{font-size:11px;line-height:14.3px;color:#333}
.readmore{font-size:11px;color:var(--title-orange);white-space:nowrap}
.contact{left:120px;top:720px;width:212px;height:236px}
.comm{left:354px;top:720px;width:210px;height:236px;background:var(--panel);border-radius:3px}
.sub-title{position:absolute;left:14px;top:11px;font-size:15px;color:#222;font-weight:400}
.field{position:absolute;left:14px;width:182px;height:24px;border:1px solid #bbb;border-radius:3px;background:linear-gradient(#fff,#e8e8e8);font-size:10px;padding:6px 5px;color:#333}
.btn{position:absolute;height:24px;border:1px solid #999;border-radius:3px;background:linear-gradient(#eee,#bbb);font-size:11px;color:#333;text-align:center;padding-top:5px}
.comm-img{left:14px;top:52px;width:182px;height:94px;background:linear-gradient(#f2f4f6,#b8c2cc 55%,#3c4654)}
.side-head{left:584px;width:208px;height:24px;background:linear-gradient(90deg,var(--orange-dark) 0,var(--orange) 12px);color:#fff;font-size:15px;padding:3px 12px}
.cal-panel{left:584px;top:441px;width:208px;height:199px;background:var(--panel);border-radius:0 0 4px 4px}
.cal{left:601px;top:459px;width:175px;background:#fff;border:1px solid #ccc;border-radius:3px;overflow:hidden}
.cal-head{height:26px;background:var(--teal);color:#fff;font:700 9px "Arimo",sans-serif;text-align:center;padding-top:8px;position:relative}
.cal-head span{position:absolute;top:5px;font-size:13px}
.cal table{border-collapse:collapse;width:175px}
.cal th{font:8px "Arimo",sans-serif;color:#999;height:17px;font-weight:400}
.cal td{border:1px solid #ddd;height:24px;width:25px;text-align:center;font-size:12px;color:#222}
.cal td.today{background:var(--teal);color:#fff}
.courses{left:597px;top:700px;width:193px;list-style:none}
.courses li{height:59px;border-bottom:1px dotted #aac;position:relative;padding-left:10px}
.courses li:last-child{border-bottom:0}
.courses li::before{content:"";position:absolute;left:0;top:5px;width:3px;height:3px;background:#555}
.courses b{display:block;font-weight:400;font-size:11px;color:#222;line-height:12px}
.courses span{display:block;font-size:10px;color:#666;line-height:14.5px;margin-top:2px}
.footer{left:0;top:980px;width:914px;height:220px;background:var(--footer);border-top:3px solid #4d6573;color:#fff}
.f-title{position:absolute;top:16px;font-size:15px;color:var(--footer-title);font-weight:400}
.f-list{position:absolute;top:40px;list-style:none;font-size:11px;line-height:17.2px}
.f-list li::before{content:"▪ ";font-size:8px;vertical-align:1px;margin-right:3px}
.social{position:absolute;top:1168px;width:18px;height:18px;background:#3a4a54;border-radius:2px}
.map{left:603px;top:1103px;width:189px;height:82px;border:2px solid #d5dde2;border-radius:3px;background:linear-gradient(120deg,#cfd8c8,#e8e4d6 50%,#c8d6e0)}
</style>
</head>
<body>
<header>
  <div class="abs topbar"></div>
  <nav class="abs nav">
    <a style="left:0">HOME</a><a style="left:87px">ABOUT US</a><a style="left:190px">COURSES</a><a style="left:294px">FACULTY</a><a style="left:394px">CONTACT US</a>
  </nav>
  <div class="abs logo"><span class="logo-name">Kali Rom</span><span class="logo-tag">Endodontic Training Center</span></div>
  <div class="abs call">
    <svg width="24" height="28" viewBox="0 0 24 28"><path d="M20 2 L8 2 Q2 2 2 10 L2 22 L7 27 L11 20 L7 16 L7 10 Q7 7 10 7 L20 7 Z" fill="#3aa9ad"/></svg>
    <span class="call-label">Call us now!</span>
    <span class="call-num">479 351 6270</span>
  </div>
</header>

<section class="abs slider">
  <div class="abs slide-img" role="img" aria-label="Lecturer teaching a classroom of dentists"></div>
  <div class="abs slide-caption">Our goal is to help you, as a dentist...</div>
  <div class="abs thumb active" style="left:13px" role="img" aria-label="Classroom lecture thumbnail"></div>
  <div class="abs thumb" style="left:156px"></div>
  <div class="abs thumb" style="left:299px"></div>
</section>

<aside class="abs next">
  <div class="next-head">Next Available Courses</div>
  <ul class="next-list">
    <li>Neque consectetur adipiscialy</li><li>Porro quisquam adipisci</li><li>Adipisci quisquam</li><li>Porro quisquam est qui</li><li>Quisquam est quisquam qui</li><li>Adipisci quisquam</li><li>Quisquam adipiscial</li>
  </ul>
</aside>

<div class="abs search"><span>Search here</span><div class="go">GO</div></div>

<section class="abs box welcome">
  <h2 class="title-orange">Welcome to Kali Rom</h2>
  <div class="dots" style="top:40px"></div>
  <div class="abs welcome-img" role="img" aria-label="Smiling professional in a suit at a desk"></div>
  <p class="abs text" style="left:200px;top:49px;width:226px">Kali Rom is part of a global network of education institution committed to the maintenace of the natural dentition. We teach endodontic &amp; restor-ative concepts and techniquies through seminars, lectures and hands-on courses in ce-nter city. Philadelphia, pannsylvania and throughout the world.</p>
  <p class="abs text" style="left:14px;top:169px;width:414px">At Next Step Endodontics, our goal is to help you, as a dentist, determine what level of endodontic knowledge and skill you currently possess and assist you in reaching your personal next level through one of our course offrings.</p>
  <p class="abs text" style="left:14px;top:226px;width:414px">Dr. Anders Holmvik is Internationally known as an endodontis and lecture. While Dr. Holmvik is now in private practice, he has spent most if his career in.</p>
  <span class="abs readmore" style="left:371px;top:256px">Read more ›</span>
</section>

<section class="abs box contact">
  <h3 class="sub-title">Quick Contact</h3>
  <div class="dots" style="top:36px;width:182px"></div>
  <div class="field" style="top:50px">Enter your name:</div>
  <div class="field" style="top:82px">Enter your email:</div>
  <div class="field" style="top:113px">Phone:</div>
  <div class="field" style="top:144px;height:46px">Massage:</div>
  <div class="btn" style="left:14px;top:197px;width:61px">SUBMIT</div>
</section>

<section class="abs comm">
  <h3 class="sub-title">Communication</h3>
  <div class="abs comm-img" role="img" aria-label="Business meeting with a handshake across a table"></div>
  <p class="abs" style="left:14px;top:156px;width:185px;font-size:9.5px;line-height:13px;color:#555">Lorem Ipsum is dummy text of the printing and typesetting industry. Lorem Ipsum since been the industry.</p>
  <span class="abs readmore" style="left:139px;top:212px">Read more ›</span>
</section>

<div class="abs side-head" style="top:417px">Calendar</div>
<div class="abs cal-panel"></div>
<div class="abs cal">
  <div class="cal-head"><span style="left:6px">‹</span>AUGUST 2012<span style="right:6px">›</span></div>
  <table>
    <tr><th>SUN</th><th>MON</th><th>TUE</th><th>WED</th><th>THU</th><th>FRI</th><th>SAT</th></tr>
    <tr><td></td><td></td><td></td><td>1</td><td>2</td><td class="today">3</td><td>4</td></tr>
    <tr><td>5</td><td>6</td><td>7</td><td>8</td><td>9</td><td>10</td><td>11</td></tr>
    <tr><td>12</td><td>13</td><td>14</td><td>15</td><td>16</td><td>17</td><td>18</td></tr>
    <tr><td>19</td><td>20</td><td>21</td><td>22</td><td>23</td><td>24</td><td>25</td></tr>
    <tr><td>26</td><td>27</td><td>28</td><td>29</td><td>30</td><td>31</td><td></td></tr>
  </table>
</div>

<div class="abs side-head" style="top:664px">Current Courses</div>
<ul class="abs courses">
  <li><b>Name of the Courses</b><span>Lorem Ipsum is simpl dummy into printing industry the industry's text.</span></li>
  <li><b>Name of the Courses</b><span>Lorem Ipsum is simpl dummy into printing industry the industry's text.</span></li>
  <li><b>Name of the Courses</b><span>Lorem Ipsum is simpl dummy into printing industry the industry's text.</span></li>
  <li><b>Name of the Courses</b><span>Lorem Ipsum is simpl dummy into printing industry the industry's text.</span></li>
</ul>
<span class="abs readmore" style="left:725px;top:931px">Read more ›</span>
<div class="abs" style="left:584px;top:955px;width:208px;border-top:1px solid #e3e3e3"></div>

<footer class="abs footer">
  <h4 class="f-title" style="left:121px">News Letter</h4>
  <p class="abs" style="left:121px;top:42px;width:180px;font-size:10px;line-height:14px">Lorem Ipsum is simpl dummy into printing industry the industry's text</p>
  <p class="abs" style="left:121px;top:78px;font-size:11.5px">Sign up to our Newsletter!</p>
  <div class="field" style="left:121px;top:97px;width:165px;height:21px;padding:4px 5px;font-size:9.5px">Enter your email...</div>
  <div class="btn" style="left:121px;top:126px;width:62px;background:linear-gradient(#dde6ea,#a9bcc6)">SUBMIT</div>
  <p class="abs" style="left:121px;top:164px;font-size:9.5px;color:#e4edf1">Copyright © 2012 Dental Education. All Rights Reserved.</p>

  <h4 class="f-title" style="left:325px">Our Courses</h4>
  <ul class="f-list" style="left:325px"><li>Lorem Ipsum is simply</li><li>including versions</li><li>industry's standard dummy</li><li>popularised</li><li>including versions</li><li>Even slightly believable</li></ul>

  <h4 class="f-title" style="left:499px">Quick Links</h4>
  <ul class="f-list" style="left:499px"><li>Home</li><li>About Us</li><li>Courses</li><li>Faculty</li><li>Contact Us</li></ul>

  <h4 class="f-title" style="left:603px">Contact Us</h4>
  <p class="abs" style="left:603px;top:42px;width:195px;font-size:10.5px;line-height:14px">Kali Rom AS, Endodontic Teaching Center, Fjeldstads vei 17C, 0371 Oslo, Norway.</p>
  <p class="abs" style="left:603px;top:78px;font-size:11px">Phone: <span style="font-size:15px;margin-left:4px">4793516270</span></p>
  <p class="abs" style="left:603px;top:99px;font-size:11px">Email: <span style="font-size:14px;margin-left:4px">info@kalirom.example</span></p>
</footer>
<div class="abs map" role="img" aria-label="Location map"></div>
<div class="social" style="left:121px"></div>
<div class="social" style="left:147px"></div>
<div class="social" style="left:173px"></div>
<div class="social" style="left:199px"></div>
</body>
</html>
```